Sparkwell Brochure site for a cleaning company based in the UK

We need a site that can sell our products and services to both attract new customer and new cleaners, It needs to be simple but informative and will link to a separate booking site already written. It preferable needs to be written in wordpress and we would require the homepage and template designed, with rights to all images and fonts.

Sparkwell is a cleaning services site offering the domestic client the ability to select from multiple cleaners and it uses our years of industry knowledge to identify the cleaners needs and match that to the correct cleaner and for the most appropriate time. Therefore the site needs to specifically target our customers whilst attracting new cleaners.

The brochure site needs to sell our services and the unique USP of our matching algorithms. This is particularly important for potential cleaners as we only offer them jobs that match their availability profile and their specific skills.

We have an existing booking site and we have attached 2 screenshots detailing the colour scheme and the feel of the site. This brochure site must match these colours and its look and feel.

The site needs to be designed on a mobile first approach as our targeted audience are mobile heavy users. It must also work across as many modern devices as possible.

Target Market(s)

UK Domestic maid cleaning

Industry/Entity Type

Cleaning Service

Coding

Coded - Design and coding required

Number of Pages Required

2 page

Font styles to use
Sans Serif

Requirements
Must have
• Attached Logo
• Menu system with the following pages (pages not designed but menu working)
• - Company Profile
• - Our Service
• - Contact Us
• - Why Sparkwell - both for customers and cleaners
• - Areas we work
• - Want to be a cleaner
• Wordpress site with the following
• - Homepage fully designed with images and font
• - The page template created
• Fully responsive design across all devices (Mobile first)
• See attached screenshots of the booking site for an idea on the colour scheme that needs to be followed.
• Photos and images
Nice to have
• Map for contact us and Areas we work

```html
<!DOCTYPE html>
<html lang="en">
<head>
<meta charset="utf-8">
<title>Sparkwell Cleaning Services</title>
<link href="https://fonts.googleapis.com/css2?family=Roboto+Condensed:wght@400;700&family=Open+Sans:wght@400;600&display=swap" rel="stylesheet">
<style>
:root{
  --green:#8fbf24;
  --green-dark:#7aa81a;
  --ink:#2b2b2b;
  --muted:#555;
  --dark:#1b1d1c;
  --footer:#262626;
  --footer-bottom:#1d1d1d;
  --white:#fff;
}
*{box-sizing:border-box;margin:0;padding:0}
html,body{width:1200px;height:2908px;overflow:hidden}
body{position:relative;background:var(--white);font-family:"Open Sans",Arial,sans-serif;color:var(--ink)}
.abs{position:absolute}
.cond{font-family:"Roboto Condensed","Arial Narrow",sans-serif}

/* hero */
.hero-photo{left:0;top:0;width:1200px;height:660px;background:radial-gradient(ellipse at 70% 30%,#8c8a55 0%,#5a5a33 35%,#3a3322 70%,#2a2418 100%)}
.hero-shade{left:0;top:0;width:1200px;height:660px;background:linear-gradient(90deg,rgba(0,0,0,.05) 0%,rgba(0,0,0,.1) 55%,rgba(0,0,0,.35) 100%)}
.brand{left:97px;top:60px;display:flex;align-items:center;gap:12px}
.brand-dot{width:46px;height:46px;border-radius:50%;background:var(--green)}
.brand-name{font-family:"Open Sans",sans-serif;font-weight:600;font-size:30px;color:var(--white)}
.call{left:684px;top:52px;color:var(--white);font-size:16px;display:flex;align-items:center;gap:10px}
.call-ico{width:30px;height:30px;border:2px solid var(--white);border-radius:50%;display:flex;align-items:center;justify-content:center}
.btn-reg{left:932px;top:50px;width:84px;height:30px;background:var(--green);color:var(--white);font-size:12px;display:flex;align-items:center;justify-content:center}
.btn-sign{left:1027px;top:50px;width:72px;height:30px;border:1px solid var(--white);color:var(--white);font-size:12px;display:flex;align-items:center;justify-content:center}
.nav{left:403px;top:114px;display:flex;gap:29px;list-style:none}
.nav li{color:var(--white);font-size:14px;font-weight:700;text-transform:uppercase;font-family:"Roboto Condensed",sans-serif}
.hero-title{left:746px;top:268px;color:var(--white);font-family:"Roboto Condensed",sans-serif;font-weight:700;line-height:1.05}
.hero-title .l1{font-size:46px;display:block}
.hero-title .l2{font-size:42px;display:block}
.hero-text{left:746px;top:374px;width:360px;color:var(--white);font-size:12px;line-height:1.6}
.dots{left:746px;top:454px;display:flex;gap:8px;align-items:center}
.dots span{width:10px;height:10px;border-radius:50%;background:var(--white)}
.dots span.on{width:16px;height:16px;border:2px solid var(--white);background:transparent;position:relative}
.dots span.on::after{content:"";position:absolute;left:3px;top:3px;width:6px;height:6px;border-radius:50%;background:var(--white)}

/* welcome */
.welcome{left:0;top:650px;width:1200px;height:364px;background:linear-gradient(180deg,#92c026,#8bbb22)}
.wave-top{left:0;top:600px}
.welcome h1{position:absolute;left:0;top:58px;width:1200px;text-align:center;color:var(--white);font-family:"Roboto Condensed",sans-serif;font-weight:400;font-size:40px}
.welcome p{position:absolute;left:190px;width:820px;text-align:center;color:var(--white);font-size:11px;line-height:1.75}
.welcome .p1{top:128px}
.welcome .p2{top:200px}
.btn-more{position:absolute;left:540px;top:264px;width:120px;height:32px;border:2px solid var(--white);border-radius:16px;color:var(--white);font-size:12px;display:flex;align-items:center;justify-content:center}

/* tasks */
.sec-title{width:1200px;left:0;text-align:center;font-family:"Roboto Condensed",sans-serif;font-size:29px;color:var(--ink)}
.task{width:230px;text-align:center}
.task svg{display:block;margin:0 auto}
.task h3{margin-top:22px;font-family:"Roboto Condensed",sans-serif;font-weight:400;font-size:16px;color:var(--ink)}
.task p{margin-top:6px;font-size:12px;line-height:1.55;color:var(--muted)}
.task .click{margin-top:14px;font-size:12px;color:var(--ink);display:inline-flex;align-items:center;gap:6px}
.arrow-dot{width:12px;height:12px;border-radius:50%;background:var(--ink);display:inline-flex;align-items:center;justify-content:center}

/* cleaner */
.cleaner{left:0;top:1566px;width:1200px;height:543px;background:radial-gradient(ellipse at 50% 30%,#2e3230 0%,#1b1d1c 70%)}
.cleaner h2{position:absolute;left:0;top:60px;width:1200px;text-align:center;color:var(--white);font-family:"Roboto Condensed",sans-serif;font-weight:400;font-size:29px}
.cleaner .rule{position:absolute;left:553px;top:118px;width:94px;height:2px;background:var(--white)}
.card{position:absolute;top:163px;width:308px;background:var(--white)}
.card .photo{height:189px}
.card h3{margin-top:14px;text-align:center;font-family:"Roboto Condensed",sans-serif;font-weight:400;font-size:21px;color:var(--ink)}
.card p{padding:6px 18px 18px;text-align:center;font-size:12px;line-height:1.6;color:var(--muted)}

/* news */
.news-title{left:98px;top:2178px;font-family:"Roboto Condensed",sans-serif;font-size:27px;color:var(--ink)}
.news-arrows{left:1062px;top:2186px;display:flex;gap:14px}
.news{position:absolute;top:2252px;display:flex;gap:26px}
.news .photo{width:187px;height:164px;flex:none}
.news .body{width:260px}
.news h3{font-family:"Roboto Condensed",sans-serif;font-weight:400;font-size:16px;line-height:1.3;color:var(--ink)}
.news .date{margin-top:10px;font-size:12px;color:var(--green)}
.news p{margin-top:12px;font-size:11px;line-height:1.6;color:var(--muted)}
.news .more{margin-top:10px;font-size:12px;color:var(--ink)}

/* footer */
.footer{left:0;top:2548px;width:1200px;height:282px;background:var(--footer)}
.wave-foot{left:0;top:2520px}
.foot-mark{left:110px;top:2600px;display:flex;flex-direction:column;align-items:center;gap:14px}
.foot-mark .disc{width:120px;height:120px;border-radius:50%;background:var(--green)}
.foot-mark span{color:var(--white);font-weight:600;font-size:22px}
.foot-col h4{font-family:"Roboto Condensed",sans-serif;font-weight:400;font-size:19px;color:var(--white);text-transform:uppercase}
.foot-col p,.foot-col li{color:#e6e6e6;font-size:12px;line-height:1.6}
.news-in{margin-top:18px;width:226px;height:40px;background:var(--white);font-size:11px;color:#777;padding:0 14px;display:flex;align-items:center}
.subscribe{margin-top:8px;width:103px;height:40px;background:var(--green);color:var(--white);font-size:12px;display:flex;align-items:center;justify-content:center}
.contact-row{display:flex;align-items:center;gap:14px;margin-top:14px}
.socials{display:flex;gap:8px;margin-top:16px}
.socials span{width:26px;height:26px;border:1.5px solid var(--white);border-radius:50%}
.links{list-style:none;margin-top:18px}
.links li{display:flex;align-items:center;gap:10px;line-height:22px}
.links li::before{content:"";border-left:6px solid var(--white);border-top:4px solid transparent;border-bottom:4px solid transparent}
.bottom{left:0;top:2830px;width:1200px;height:78px;background:var(--footer-bottom);color:#ddd;font-size:11px;display:flex;align-items:center;justify-content:center}
</style>
</head>
<body>

<header>
  <div class="abs hero-photo" role="img" aria-label="Gloved hand wiping a window with a spray bottle of cleaner"></div>
  <div class="abs hero-shade"></div>
  <div class="abs brand"><span class="brand-dot"></span><span class="brand-name">Sparkwell</span></div>
  <div class="abs call cond">
    <span class="call-ico"><svg width="14" height="14" viewBox="0 0 24 24"><path fill="#fff" d="M6.6 10.8a15 15 0 0 0 6.6 6.6l2.2-2.2a1 1 0 0 1 1-.25 11.4 11.4 0 0 0 3.6.57 1 1 0 0 1 1 1V20a1 1 0 0 1-1 1A17 17 0 0 1 3 4a1 1 0 0 1 1-1h3.5a1 1 0 0 1 1 1c0 1.25.2 2.45.57 3.57a1 1 0 0 1-.25 1z"/></svg></span>
    CALL US : +1 555 014 2290
  </div>
  <div class="abs btn-reg">REGISTER</div>
  <div class="abs btn-sign">SIGN-IN</div>
  <ul class="abs nav">
    <li>Home</li><li>Profile</li><li>Our Service</li><li>Why Sparkwell</li><li>Areas We Work</li><li>Want to be a Cleaner ?</li><li>Contact Us</li>
  </ul>
  <h1 class="abs hero-title"><span class="l1">SPARKWELL</span><span class="l2">CLEANING SERVICES</span></h1>
  <p class="abs hero-text">Sed ut perspiciatis unde omnis iste natus error sit voluptatem accusantium doloremque laudantium, totam rem aperiam, eaque ipsa quae</p>
  <div class="abs dots"><span class="on"></span><span></span><span></span><span></span></div>
</header>

<svg class="abs wave-top" width="1200" height="60" viewBox="0 0 1200 60"><path d="M0 30 C220 -5 420 40 640 28 C860 16 1000 0 1200 12 V60 H0Z" fill="#92c026"/></svg>
<section class="abs welcome">
  <h1>Welcome to Sparkwell</h1>
  <p class="p1">Lorem ipsum dolor sit amet, consectetur adipiscing elit, sed do eiusmod tempor incididunt ut labore et dolore magna aliqua. Ut enim ad minim veniam, quis nostrud exercitation ullamco laboris nisi ut aliquip ex ea commodo consequat. Duis aute irure dolor in reprehenderit in voluptate velit esse cillum dolore eu fugiat nulla pariatur. Excepteur sint occaecat cupidatat non proident, sunt in culpa qui officia deserunt mollit anim id est laborum</p>
  <p class="p2">Lorem ipsum dolor sit amet, consectetur adipiscing elit, sed do eiusmod tempor incididunt ut labore et dolore magna aliqua. Ut enim ad minim veniam, quis nostrud exercitation ullamco laboris nisi ut aliquip ex ea commodo consequat. Duis aute irure dolor in reprehenderit in voluptate</p>
  <div class="btn-more">READ MORE</div>
</section>

<h2 class="abs sec-title" style="top:1100px">CHOOSE YOUR TASKS</h2>

<div class="abs task" style="left:90px;top:1196px">
  <svg width="104" height="152" viewBox="0 0 104 152"><path d="M52 2a50 50 0 0 1 50 50c0 38-50 98-50 98S2 90 2 52A50 50 0 0 1 52 2z" fill="#8fbf24"/><circle cx="52" cy="52" r="38" fill="#fff"/><path d="M64 30 48 58M38 58h20l6 16H32z" stroke="#8fbf24" stroke-width="3" fill="none" stroke-linejoin="round"/></svg>
  <h3>CLEANING SERVICES</h3>
  <p>Lorem ipsum dolor sit amet, consectetur adiscing elit, sed do eiusmod tempor incididunt ut labore et dolore</p>
  <div class="click">CLICK HERE <span class="arrow-dot"><svg width="6" height="6" viewBox="0 0 6 6"><path d="M1 0l4 3-4 3z" fill="#fff"/></svg></span></div>
</div>
<div class="abs task" style="left:355px;top:1196px">
  <svg width="104" height="152" viewBox="0 0 104 152"><path d="M52 2a50 50 0 0 1 50 50c0 38-50 98-50 98S2 90 2 52A50 50 0 0 1 52 2z" fill="#8fbf24"/><circle cx="52" cy="52" r="38" fill="#fff"/><rect x="30" y="50" width="44" height="12" rx="3" fill="#8fbf24"/><rect x="34" y="38" width="36" height="12" rx="3" fill="none" stroke="#8fbf24" stroke-width="3"/></svg>
  <h3>LINEN SERVICES</h3>
  <p>Lorem ipsum dolor sit amet, consectetur adiscing elit, sed do eiusmod tempor incididunt ut labore et dolore</p>
  <div class="click">CLICK HERE <span class="arrow-dot"><svg width="6" height="6" viewBox="0 0 6 6"><path d="M1 0l4 3-4 3z" fill="#fff"/></svg></span></div>
</div>
<div class="abs task" style="left:622px;top:1196px">
  <svg width="104" height="152" viewBox="0 0 104 152"><path d="M52 2a50 50 0 0 1 50 50c0 38-50 98-50 98S2 90 2 52A50 50 0 0 1 52 2z" fill="#8fbf24"/><circle cx="52" cy="52" r="38" fill="#fff"/><path d="M28 64h48c0-14-8-22-22-22H40v-4h26" stroke="#8fbf24" stroke-width="3" fill="none"/><path d="M28 64c2-10 12-18 26-18h14" fill="#8fbf24"/></svg>
  <h3>IRONING SERVICES</h3>
  <p>Lorem ipsum dolor sit amet, consectetur adiscing elit, sed do eiusmod tempor incididunt ut labore et dolore</p>
  <div class="click">CLICK HERE <span class="arrow-dot"><svg width="6" height="6" viewBox="0 0 6 6"><path d="M1 0l4 3-4 3z" fill="#fff"/></svg></span></div>
</div>
<div class="abs task" style="left:881px;top:1196px">
  <svg width="104" height="152" viewBox="0 0 104 152"><path d="M52 2a50 50 0 0 1 50 50c0 38-50 98-50 98S2 90 2 52A50 50 0 0 1 52 2z" fill="#8fbf24"/><circle cx="52" cy="52" r="38" fill="#fff"/><rect x="38" y="28" width="28" height="46" rx="3" fill="#8fbf24"/><path d="M38 44h28M44 34v6M44 50v8" stroke="#fff" stroke-width="2.5"/></svg>
  <h3>FRIDGE FREEZER</h3>
  <p>Lorem ipsum dolor sit amet, consectetur adiscing elit, sed do eiusmod tempor incididunt ut labore et dolore</p>
  <div class="click">CLICK HERE <span class="arrow-dot"><svg width="6" height="6" viewBox="0 0 6 6"><path d="M1 0l4 3-4 3z" fill="#fff"/></svg></span></div>
</div>

<section class="abs cleaner">
  <h2>WANT TO BE A CLEANER ?</h2>
  <div class="rule"></div>
  <article class="card" style="left:103px">
    <div class="photo" role="img" aria-label="Team of cleaners scrubbing an outdoor paved floor with machines" style="background:linear-gradient(160deg,#6f8a55,#a4a8a0 55,#8c8f88)"></div>
    <h3>Sed ut perspiciatis unde</h3>
    <p>Lorem ipsum dolor sit amet, consectetur adipiscing elit, sed do eiusmod tempor incididunt ut labore et dolore magna aliqua. Ut enim ad minim</p>
  </article>
  <article class="card" style="left:446px">
    <div class="photo" role="img" aria-label="Cleaner in yellow gloves cleaning a kitchen oven" style="background:linear-gradient(160deg,#6b5e52,#b89e88 55%,#8a7a6c)"></div>
    <h3>Sed ut perspiciatis unde</h3>
    <p>Lorem ipsum dolor sit amet, consectetur adipiscing elit, sed do eiusmod tempor incididunt ut labore et dolore magna aliqua. Ut enim ad minim</p>
  </article>
  <article class="card" style="left:788px">
    <div class="photo" role="img" aria-label="Man ironing laundry in a bright living room" style="background:linear-gradient(160deg,#c9ccd2,#7f9bc0 55%,#b7b2ae)"></div>
    <h3>Sed ut perspiciatis unde</h3>
    <p>Lorem ipsum dolor sit amet, consectetur adipiscing elit, sed do eiusmod tempor incididunt ut labore et dolore magna aliqua. Ut enim ad minim</p>
  </article>
</section>

<h2 class="abs news-title">LATEST NEWS</h2>
<div class="abs news-arrows">
  <svg width="12" height="10" viewBox="0 0 12 10"><path d="M11 5H2M5 1 1 5l4 4" stroke="#333" stroke-width="1.5" fill="none"/></svg>
  <svg width="12" height="10" viewBox="0 0 12 10"><path d="M1 5h9M7 1l4 4-4 4" stroke="#333" stroke-width="1.5" fill="none"/></svg>
</div>
<article class="news" style="left:98px">
  <div class="photo" role="img" aria-label="Woman mopping a living room floor" style="background:linear-gradient(160deg,#e6e2dc,#c4b8a8 60%,#9a8e80)"></div>
  <div class="body">
    <h3>Sed ut perspiciatis unde omnis iste natus error sit voluptatem</h3>
    <div class="date">JAN 29, 2017</div>
    <p>Nulla at diam ornare, aliquam urna vel, commodo urna. Nam id risus a est luctus consectetur quis eget libero. Suspendisse potenti. Pellentesque</p>
    <div class="more">Read More +</div>
  </div>
</article>
<article class="news" style="left:630px">
  <div class="photo" role="img" aria-label="Gloved hands cleaning a surface with a spray bottle" style="background:linear-gradient(160deg,#4a4540,#7a6a5c 55%,#a03a2c)"></div>
  <div class="body">
    <h3>Sed ut perspiciatis unde omnis iste natus error sit voluptatem</h3>
    <div class="date">JAN 29, 2017</div>
    <p>Nulla at diam ornare, aliquam urna vel, commodo urna. Nam id risus a est luctus consectetur quis eget libero. Suspendisse potenti. Pellentesque</p>
    <div class="more">Read More +</div>
  </div>
</article>

<svg class="abs wave-foot" width="1200" height="40" viewBox="0 0 1200 40"><path d="M0 28 C200 10 380 4 600 16 C820 28 1000 30 1200 10 V40 H0Z" fill="#262626"/></svg>
<footer>
  <div class="abs footer"></div>
  <div class="abs foot-mark"><span class="disc"></span><span>Sparkwell</span></div>
  <div class="abs foot-col" style="left:348px;top:2578px">
    <h4>Newsletter Signup</h4>
    <p style="margin-top:14px;width:220px;font-size:11px">Excepteur sint occaecat cupidatat non proident, sunt in culpa qui</p>
    <div class="news-in">Enter email</div>
    <div class="subscribe">SUBSCRIBE</div>
  </div>
  <div class="abs foot-col" style="left:660px;top:2578px">
    <h4>Contact Us</h4>
    <p style="margin-top:14px">Sparkwell<br>No 27 Meadow Lane, Brookfield, BR4 7LD</p>
    <div class="contact-row">
      <svg width="16" height="16" viewBox="0 0 24 24"><path fill="#fff" d="M6.6 10.8a15 15 0 0 0 6.6 6.6l2.2-2.2a1 1 0 0 1 1-.25 11.4 11.4 0 0 0 3.6.57 1 1 0 0 1 1 1V20a1 1 0 0 1-1 1A17 17 0 0 1 3 4a1 1 0 0 1 1-1h3.5a1 1 0 0 1 1 1c0 1.25.2 2.45.57 3.57a1 1 0 0 1-.25 1z"/></svg>
      <p>Call Us 555.017.3381</p>
    </div>
    <div class="contact-row">
      <svg width="16" height="12" viewBox="0 0 16 12"><rect x=".75" y=".75" width="14.5" height="10.5" fill="none" stroke="#fff" stroke-width="1.5"/><path d="M1 1l7 6 7-6" fill="none" stroke="#fff" stroke-width="1.5"/></svg>
      <p>info@sparkwell.com</p>
    </div>
    <div class="socials"><span></span><span></span><span></span><span></span></div>
  </div>
  <div class="abs foot-col" style="left:957px;top:2578px">
    <h4>Quick Links</h4>
    <ul class="links">
      <li>Home</li><li>Profile</li><li>Our Service</li><li>Why Sparkwell</li><li>Areas we work</li><li>Want to be a cleaner ?</li><li>Contact Us</li>
    </ul>
  </div>
  <div class="abs bottom">2017 © Copyrights Sparkwell.All Rights Reserved</div>
</footer>

</body>
</html>
```